Courier company needs a Facebook page

Swift Lantern Courier & Delivery Services is a new company and I need a Facebook page. We will be handling small deliveries up to 20 pounds. We aim to have 70 percent of our business from commercial clients and 30 percent from residential clients. We promise 100 % customer satisfaction and offer our services 24 hours a day 7 days a week 365 days a year . We will only be delivering within Yellowknife, NWT , Canada. Our tag line is On Time Every Time.

Target Market(s)

Professional types

Industry/Entity Type

Residential

Requirements
Must have
• My facebook page is blank so I need all the areas covered. The large banner picture should really catch my eye and convey speed of delivery or perhaps a skyline view of Yellowknife, NWT, Canada. Another possibility is to show the spectacular northern lights that Yellowknife is famous for.
Nice to have
• I would probably like a stunning picture that has something to do with delivering for the large area and perhaps my logo in the smaller picture.

```html
<!DOCTYPE html>
<html lang="en">
<head>
<meta charset="utf-8">
<title>Swift Lantern Courier & Delivery Services – Cover</title>
<link rel="stylesheet" href="https://fonts.googleapis.com/css2?family=Oswald:wght@600&family=Roboto+Condensed:wght@400;700&display=swap">
<style>
  :root {
    --red: #e3202a;
    --blue: #1d5fae;
    --green: #5db533;
    --rule: #d6d9de;
    --white: #ffffff;
    --shirt-light: #e6eef7;
    --shirt-mid: #c3d4e8;
    --paper: #e7c58e;
    --gold: #e3b23c;
    --gold-dark: #b9861e;
  }
  * { margin: 0; padding: 0; box-sizing: border-box; }
  html, body { width: 1200px; height: 444px; overflow: hidden; background: var(--white); }
  .cover {
    position: relative;
    width: 1200px;
    height: 444px;
    overflow: hidden;
    background: var(--white);
    font-family: "Roboto Condensed", "Arial Narrow", sans-serif;
  }
  .cover-photo {
    position: absolute;
    left: 0; top: 0;
    width: 720px; height: 444px;
    background:
      radial-gradient(ellipse 180px 140px at 90px 330px, var(--paper) 0%, rgba(231,197,142,0) 100%),
      radial-gradient(ellipse 150px 200px at 560px 330px, #f0e2c4 0%, rgba(240,226,196,0) 100%),
      linear-gradient(90deg, var(--shirt-mid) 0%, var(--shirt-light) 45%, #f4f7fb 75%, var(--white) 100%);
  }
  .brand-box {
    position: absolute;
    left: 0; top: 8px;
    width: 398px; height: 172px;
    background: var(--white);
    display: flex;
    align-items: center;
    padding: 0 24px;
  }
  .brand-name {
    font-weight: 700;
    font-size: 38px;
    line-height: 1.05;
    color: var(--red);
    text-transform: uppercase;
  }
  .guarantee-ribbon {
    position: absolute;
    left: 543px; top: 0;
    width: 134px; height: 134px;
    background: var(--red);
  }
  .guarantee-seal {
    position: absolute;
    left: 548px; top: 0;
  }
  .headline {
    position: absolute;
    left: 709px; top: 42px;
    font-family: "Oswald", "Arial Narrow", sans-serif;
    font-weight: 600;
    font-size: 54px;
    line-height: 1;
    color: var(--red);
    letter-spacing: 0.5px;
    white-space: nowrap;
  }
  .features {
    position: absolute;
    left: 695px; top: 135px;
    width: 460px;
    list-style: none;
  }
  .feature {
    display: flex;
    align-items: center;
    height: 96px;
    border-bottom: 1.5px solid var(--rule);
  }
  .feature:last-child { border-bottom: none; }
  .feature-icon { flex: 0 0 auto; width: 58px; height: 58px; margin-left: 4px; }
  .feature-text {
    margin-left: 14px;
    font-size: 24px;
    line-height: 31px;
    color: var(--blue);
    text-transform: uppercase;
    letter-spacing: 0.3px;
  }
  .feature-text strong { font-weight: 700; }
</style>
</head>
<body>
<div class="cover">
  <div class="cover-photo" role="img" aria-label="Courier in a light blue shirt holding a clipboard and a parcel"></div>

  <div class="brand-box">
    <p class="brand-name">Swift Lantern<br>Courier &amp; Delivery Services</p>
  </div>

  <div class="guarantee-ribbon"></div>
  <svg class="guarantee-seal" width="124" height="124" viewBox="0 0 124 124" aria-hidden="true">
    <circle cx="62" cy="62" r="58" fill="var(--gold)"/>
    <circle cx="62" cy="62" r="44" fill="var(--white)" stroke="var(--gold-dark)" stroke-width="3"/>
    <circle cx="62" cy="62" r="30" fill="var(--gold)"/>
  </svg>

  <h1 class="headline">ON TIME EVERY TIME</h1>

  <ul class="features">
    <li class="feature">
      <svg class="feature-icon" viewBox="0 0 58 58" aria-hidden="true">
        <circle cx="29" cy="29" r="27" fill="var(--green)"/>
        <circle cx="29" cy="29" r="18" fill="none" stroke="var(--white)" stroke-width="4"/>
        <path d="M29 18 V30 H38" fill="none" stroke="var(--white)" stroke-width="4" stroke-linecap="round"/>
      </svg>
      <p class="feature-text">Our services <strong>24 hours</strong> a day<br><strong>7 days</strong> a week <strong>365 days</strong> a year</p>
    </li>
    <li class="feature">
      <svg class="feature-icon" viewBox="0 0 58 58" aria-hidden="true">
        <rect x="2" y="12" width="32" height="28" rx="2" fill="var(--green)"/>
        <path d="M36 20 H47 L56 31 V40 H36 Z" fill="var(--green)"/>
        <path d="M40 23 H46 L51 30 H40 Z" fill="var(--white)"/>
        <circle cx="14" cy="44" r="7" fill="var(--green)" stroke="var(--white)" stroke-width="3"/>
        <circle cx="45" cy="44" r="7" fill="var(--green)" stroke="var(--white)" stroke-width="3"/>
      </svg>
      <p class="feature-text">Delivering area within<br><strong>Yellowknife, NWT , Canada.</strong></p>
    </li>
    <li class="feature">
      <svg class="feature-icon" viewBox="0 0 58 58" aria-hidden="true">
        <rect x="6" y="18" width="46" height="11" fill="var(--green)"/>
        <rect x="10" y="31" width="38" height="24" fill="var(--green)"/>
        <rect x="26" y="18" width="6" height="37" fill="var(--white)"/>
        <path d="M29 17 C22 4 12 8 17 15 Z M29 17 C36 4 46 8 41 15 Z" fill="var(--green)"/>
      </svg>
      <p class="feature-text">Handling small deliveries<br>up to <strong>20 pounds</strong></p>
    </li>
  </ul>
</div>
</body>
</html>
```